Business Card Design Project

New Private residential substance abuse treatment facility in Mapleton, UT. Facility located in elegant 11,000 home with stunning views of the mountains. Wish to incorporate colored logo. Business name- Cedar Brook Wellness. Facility is Tudor style with traditional furnishings, an overhead picture is attached. Lettering in a simple scroll or old english style. Must be easy to read with clear moderetly large font.
Updates

It seems the project time frame listed was not correct- it is a week.

Target Market(s)

Adults 18 and over with substance abuse issues requiring residential rehabilitation. Referral base are medical/mental health professionals, families and community agencies.

Industry/Entity Type

Residential

Colors
9bcb3b
fece3e
fbee3f

Requirements
Must have
• Clear and easy to read, professional and upscale presentation. Need logo, name, title, address, phone, fax and web page address. May add slogan later. Use same font as logo.
Nice to have
• Logo has a green mountain and a gold maple leaf so a nature themed element may work. Want to promote peaceful grounded image. Logo attached.
Should not have
• No tiny or complicated font. No modern or tech looking images. No light colored fonts.

```html
<!DOCTYPE html>
<html lang="en">
<head>
<meta charset="utf-8">
<title>Cedar Brook Wellness – Business Card</title>
<link rel="stylesheet" href="https://fonts.googleapis.com/css2?family=Exo+2:wght@400;600;700&family=Gochi+Hand&display=swap">
<style>
  :root {
    --bg: #8a8a8a;
    --card: #ffffff;
    --forest: #3f6a22;
    --gold: #d4a02a;
    --ink: #222222;
    --rule: #1f1f1f;
  }
  * { box-sizing: border-box; margin: 0; padding: 0; }
  html, body {
    width: 1200px; height: 1012px; overflow: hidden;
    background: var(--bg);
  }
  .card {
    position: absolute; left: 60px; top: 197px;
    width: 1080px; height: 617px;
    background: var(--card);
    overflow: hidden;
    font-family: "Exo 2", sans-serif;
    color: var(--ink);
    box-shadow: 0 10px 30px rgba(0,0,0,.25);
  }
  .brand {
    position: absolute; left: 50px; top: 62px;
    display: flex; align-items: center; gap: 14px;
  }
  .brand-mark {
    width: 22px; height: 22px; border-radius: 50%;
    background: var(--forest);
  }
  .brand-name {
    font-size: 34px; font-weight: 600; color: var(--forest);
    letter-spacing: .5px;
  }
  .top-rule {
    position: absolute; left: 40px; top: 140px;
    width: 600px; height: 2px; background: var(--rule);
  }
  .slogan {
    position: absolute; right: 60px; top: 66px;
    text-align: right;
    font-family: "Gochi Hand", cursive;
    font-size: 30px; line-height: 36px; color: var(--forest);
  }
  .title {
    position: absolute; right: 230px; top: 178px;
    font-size: 22px; font-weight: 600; color: var(--gold);
  }
  .title-rule {
    position: absolute; left: 880px; top: 192px;
    width: 60px; height: 2px; background: var(--rule);
  }
  .person {
    position: absolute; left: 50px; top: 168px;
    z-index: 2;
  }
  .person-name { font-size: 32px; font-weight: 700; margin-bottom: 10px; }
  .contact { font-size: 19px; line-height: 29px; }
  .social {
    position: absolute; right: 130px; top: 250px;
    font-size: 19px; color: var(--forest);
  }
  .social-row {
    display: flex; align-items: center; justify-content: flex-end;
    gap: 12px; height: 50px;
  }
  .social-row .lead { color: var(--ink); }
  .social-tile {
    width: 36px; height: 36px; border: 2px solid var(--forest); border-radius: 5px;
  }
  .website {
    position: absolute; right: 110px; top: 372px;
    font-size: 25px; font-weight: 700; color: var(--forest);
  }
  .treeline {
    position: absolute; left: 0; top: 330px; width: 660px; height: 232px;
  }
  .bands { position: absolute; left: 0; bottom: 0; width: 1080px; height: 60px; }
</style>
</head>
<body>
  <main class="card">
    <div class="brand">
      <span class="brand-mark"></span>
      <span class="brand-name">Cedar Brook Wellness</span>
    </div>
    <div class="top-rule"></div>

    <p class="slogan">Earth Allows You to Stand.<br>Let the Earth Stand the Way It Is</p>
    <p class="title">Chief Executive Officer</p>
    <div class="title-rule"></div>

    <svg class="treeline" viewBox="0 0 660 232" preserveAspectRatio="none" role="img" aria-label="Silhouette of a green forest treeline along the bottom edge">
      <defs>
        <linearGradient id="forestFadeV" x1="0" y1="0" x2="0" y2="1">
          <stop offset="0" stop-color="#7fa264" stop-opacity="0"/>
          <stop offset=".5" stop-color="#7fa264" stop-opacity=".45"/>
          <stop offset="1" stop-color="#5d8743" stop-opacity=".85"/>
        </linearGradient>
        <linearGradient id="forestFadeH" x1="0" y1="0" x2="1" y2="0">
          <stop offset="0" stop-color="#fff" stop-opacity="1"/>
          <stop offset=".85" stop-color="#fff" stop-opacity="1"/>
          <stop offset="1" stop-color="#fff" stop-opacity="0"/>
        </linearGradient>
        <mask id="forestEdge"><rect width="660" height="232" fill="url(#forestFadeH)"/></mask>
      </defs>
      <rect width="660" height="232" fill="url(#forestFadeV)" mask="url(#forestEdge)"/>
    </svg>

    <section class="person">
      <h1 class="person-name">Dr. Helen Marsh</h1>
      <p class="contact">1420 Ridge View Dr, Mapleton, UT</p>
      <p class="contact">OFC 312 - 555 - 0148</p>
      <p class="contact">FAX 312 - 555 - 0149</p>
      <p class="contact">+61400 555 218</p>
      <p class="contact">hello@cedarbrookwellness.com</p>
    </section>

    <section class="social">
      <div class="social-row"><span class="lead">Join our campaign on</span><span class="social-tile"></span><span>/cedarbrookwellness</span></div>
      <div class="social-row"><span class="social-tile"></span><span>@cedarbrook</span></div>
    </section>
    <p class="website">Visit our website: www.cedarbrookwellness.com</p>

    <svg class="bands" viewBox="0 0 1080 60">
      <polygon points="0,2 620,2 670,36 0,36" fill="var(--forest)"/>
      <polygon points="680,20 1080,20 1080,60 720,60" fill="var(--gold)"/>
    </svg>
  </main>
</body>
</html>
```